Talking Points for Clinic Visits tri-fold brochure

We are looking for a 1 page (front and back) 8.5" x 11" tri-fold brochure. Please refer back to our Rack Cards for a similar look and feel to the design. They can be found here: https://venmorelink.org/resources/fresh-plate-steady-mind-rack-card-series/.
This brochure is titled: Talking Points for Clinic Visits on Recall Lapses.

The document is for older readers. Do not put text over graphics and keep it simple and easy to read with high contrast.

We want some very simple design element(s) incorporated that convey Native American communities or heritage. But NO headdress, teepee graphics, owls etc. I have included some images, please use your creative discretion to use which ones look good.

Please remember to include the funding statement - it can be in a very small font 6/7 point: For more information about our project, please visit https://venmorelink.org/mind-care/resources - This rack card is supported by the Bureau for Illness Tracking and Safeguards (BITS) of the Federal Office of Wellness and Civic Aid (OWCA) as part of a financial assistance award totaling $1,053,119.36 with 100 percent funded by BITS/OWCA. The contents are those of the author(s) and do not necessarily represent the official views of, nor an endorsement, by BITS/OWCA, or the Venmore Federal Council.

Please feel free to choose one of each of the 2 logos that looks best (horizontal or square). We have the VL7 logo and the Mind Care Support Hub logo we would like to add. I have added the document and there are images to choose from to use.

I am thinking that the front of the tri-fold should have one of the pictures of a patient and doctor talking. I have included several options. Please use your creative discretion to choose what looks best.

Please let me know if you have any questions, thank you!

```html
<!DOCTYPE html>
<html lang="en">
<head>
<meta charset="utf-8">
<title>Talking Points for Clinic Visits on Recall Lapses – Tri-fold</title>
<link rel="stylesheet" href="https://fonts.googleapis.com/css2?family=Montserrat:wght@600;700&family=Quicksand:wght@500;600;700&display=swap">
<style>
  :root{
    --bg:#e9e9eb;
    --paper:#ffffff;
    --ink:#1d1d1f;
    --teal-dark:#1f3e40;
    --teal:#2f6d70;
    --brown:#5b2f28;
    --rust:#b0594c;
    --gold:#dcb46c;
    --sky:#bcd3ee;
    --grey-line:#555;
  }
  *{box-sizing:border-box;margin:0;padding:0}
  html,body{width:788px;height:1200px;overflow:hidden;background:var(--bg)}
  body{font-family:"Quicksand",sans-serif;color:var(--ink);position:relative}
  .spread{position:absolute;left:24px;width:740px;height:572px;background:var(--paper);display:grid;grid-template-columns:247px 246px 247px;box-shadow:0 4px 14px rgba(0,0,0,.18)}
  .spread--outside{top:19px}
  .spread--inside{top:609px}
  .panel{position:relative;overflow:hidden}
  .band{position:absolute;left:0;right:0;height:8px;display:flex}
  .band--top{top:0}.band--bottom{bottom:0}
  .band span{display:block;height:100%}
  .c-brown{background:var(--brown)}.c-teal{background:var(--teal)}.c-rust{background:var(--rust)}.c-dark{background:var(--teal-dark)}

  /* outside: tracker */
  .tracker{padding:30px 20px 20px}
  .tracker__title{font-family:"Montserrat",sans-serif;font-weight:600;font-size:13px;margin-bottom:10px}
  .tracker p{font-size:9.5px;line-height:1.4;font-weight:500;margin-bottom:10px}
  .tracker__rule{border-top:1px dashed var(--grey-line);margin:18px 0 14px}
  .tracker__table{width:100%;border-collapse:collapse;font-size:7.5px;font-weight:700}
  .tracker__table th,.tracker__table td{border:1px solid var(--grey-line);height:19px;padding:0 4px;text-align:left}
  .tracker__table th{height:22px}

  /* outside: resources */
  .resources{background:var(--teal-dark);color:#fff;padding:30px 18px 14px;text-align:center;display:flex;flex-direction:column}
  .resources__title{font-family:"Montserrat",sans-serif;font-weight:700;font-size:17px;line-height:1.2;margin-bottom:16px}
  .resource{margin-bottom:11px}
  .resource__name{font-family:"Montserrat",sans-serif;font-weight:700;color:var(--gold);font-size:10px;line-height:1.3}
  .resource__link{font-size:9.5px;font-weight:500;margin-top:4px}
  .funding{margin-top:auto;font-size:5px;line-height:1.35;color:#d7dede}
  .funding p+p{margin-top:3px}

  /* outside: cover */
  .cover{padding:28px 18px 0;display:flex;flex-direction:column}
  .brand{color:var(--teal-dark);font-family:"Quicksand",sans-serif;font-weight:700;font-size:10px;line-height:1.25;text-align:right}
  .cover__title{font-family:"Montserrat",sans-serif;font-weight:700;color:var(--teal-dark);font-size:20px;line-height:1.2;text-align:center;margin:22px 0 16px}
  .cover__art{flex:1;margin:0 -18px;background:linear-gradient(180deg,#f4f4f4 0%,#c9c9cb 55%,#a7a39f 100%)}

  /* inside: intro */
  .intro{background:var(--sky);display:flex;flex-direction:column}
  .intro__text{padding:28px 16px 10px;text-align:center;font-size:9.3px;line-height:1.38;font-weight:500}
  .intro__text p+p{margin-top:10px}
  .intro__photo{flex:1;background:linear-gradient(180deg,#a9c4df 0%,#7aa070 45%,#4f6e3d 100%)}

  /* inside: talking points */
  .points{display:flex;flex-direction:column}
  .points__photo{height:128px;background:linear-gradient(135deg,#d8cfc9 0%,#a08c87 50%,#5e5275 100%)}
  .points__body{flex:1;background:var(--brown);color:#fff;padding:24px 14px 14px;position:relative}
  .points__title{font-family:"Montserrat",sans-serif;font-weight:700;font-size:11.5px;margin-bottom:10px}
  .points ol{list-style:none}
  .points ol>li{display:grid;grid-template-columns:16px 1fr;gap:4px;font-size:9px;line-height:1.32;font-weight:600;margin-bottom:8px}
  .num{width:13px;height:13px;border-radius:50%;background:#8fb8bb;color:var(--brown);font-size:8px;font-weight:700;display:flex;align-items:center;justify-content:center}
  .points ul{list-style:none;margin-top:2px}
  .points ul li{padding-left:8px;position:relative;font-weight:500}
  .points ul li::before{content:"•";position:absolute;left:0}

  /* inside: doctor questions */
  .asks{display:flex;flex-direction:column}
  .asks__text{padding:24px 12px 8px 14px}
  .asks__title{font-family:"Montserrat",sans-serif;font-weight:600;font-size:11.5px;line-height:1.3}
  .asks__by{font-size:9.3px;font-weight:500;margin-bottom:14px}
  .asks ul{list-style:none}
  .asks li{position:relative;padding-left:13px;font-size:9px;line-height:1.6;font-weight:600}
  .asks li::before{content:"";position:absolute;left:0;top:4px;width:8px;height:8px;border-radius:50%;background:var(--brown)}
  .asks__photo{flex:1;background:linear-gradient(180deg,#ffffff 0%,#e2e4e6 30%,#c9ccd0 70%,#b7b9bd 100%)}
</style>
</head>
<body>

<section class="spread spread--outside" aria-label="Brochure outside">
  <div class="panel tracker">
    <div class="band band--top"><span class="c-dark" style="width:60px"></span><span class="c-teal" style="width:40px"></span><span class="c-brown" style="flex:1"></span></div>
    <h2 class="tracker__title">Symptom Tracking:</h2>
    <p>By tracking symptoms like forgetfulness, confusion, or difficulty with everyday tasks, individuals and their caregivers can provide accurate information to healthcare providers, leading to better planning and support.</p>
    <p>A symptom tracker template and examples can be found at :</p>
    <div class="tracker__rule"></div>
    <table class="tracker__table">
      <thead><tr><th style="width:22%">Date</th><th style="width:20%">Time</th><th style="width:22%">Location</th><th>Symptoms &amp; Behavior</th></tr></thead>
      <tbody>
        <tr><td></td><td></td><td></td><td></td></tr><tr><td></td><td></td><td></td><td></td></tr>
        <tr><td></td><td></td><td></td><td></td></tr><tr><td></td><td></td><td></td><td></td></tr>
        <tr><td></td><td></td><td></td><td></td></tr><tr><td></td><td></td><td></td><td></td></tr>
        <tr><td></td><td></td><td></td><td></td></tr><tr><td></td><td></td><td></td><td></td></tr>
        <tr><td></td><td></td><td></td><td></td></tr><tr><td></td><td></td><td></td><td></td></tr>
        <tr><td></td><td></td><td></td><td></td></tr><tr><td></td><td></td><td></td><td></td></tr>
      </tbody>
    </table>
    <div class="band band--bottom"><span class="c-brown" style="width:150px"></span><span class="c-teal" style="width:40px"></span><span class="c-brown" style="flex:1"></span></div>
  </div>

  <div class="panel resources">
    <div class="band band--top"><span class="c-teal" style="width:80px"></span><span class="c-rust" style="flex:1"></span></div>
    <h2 class="resources__title">For More Information About Memory Loss</h2>
    <div class="resource"><div class="resource__name">10 Signs of Thinking or Memory Changes that Might be Dementia:</div><div class="resource__link">https://lnk.vl/10SignsVenmore</div></div>
    <div class="resource"><div class="resource__name">Memory Companions Room:</div><div class="resource__link">venmorelink.org/memory-companions/rooms</div></div>
    <div class="resource"><div class="resource__name">Northvale Living with Memory Loss:</div><div class="resource__link">https://lnk.vl/NorthvaleRecall</div></div>
    <div class="resource"><div class="resource__name">Elder Alliance Questions to Ask:</div><div class="resource__link">https://lnk.vl/ElderAllianceQA</div></div>
    <div class="resource"><div class="resource__name">Routes to Well-Being with Dementia:</div><div class="resource__link">https://lnk.vl/WellBeingRoutes</div></div>
    <div class="funding">
      <p>For more information about our project, please visit https://venmorelink.org/mind-care/resources</p>
      <p>This rack card is supported by the Bureau for Illness Tracking and Safeguards (BITS) of the Federal Office of Wellness and Civic Aid (OWCA) as part of a financial assistance award totaling $1,053,119.36 with 100 percent funded by BITS/OWCA. The contents are those of the author(s) and do not necessarily represent the official views of, nor an endorsement, by BITS/OWCA, or the Venmore Federal Council.</p>
    </div>
  </div>

  <div class="panel cover">
    <div class="band band--top"><span style="width:180px"></span><span class="c-rust" style="flex:1"></span></div>
    <div class="brand">Venmore Link Council<br>on Native Elders</div>
    <h1 class="cover__title">Talking Points for Clinic Visits on Recall Lapses</h1>
    <div class="cover__art" role="img" aria-label="Illustration of head-shaped trees and question marks above a photo of an older man looking upward thoughtfully"></div>
  </div>
</section>

<section class="spread spread--inside" aria-label="Brochure inside">
  <div class="panel intro">
    <div class="band band--top"><span class="c-teal" style="width:130px"></span><span class="c-rust" style="flex:1"></span></div>
    <div class="intro__text">
      <p>In our communities, memory and wisdom are sacred. When our Elders begin to experience changes in how they remember, think, or act, it's important to understand what's happening, so we can care for them with knowledge, love, and respect.</p>
      <p>Memory loss can progress to dementia. Dementia is a group of conditions that affect memory, thinking, and the ability to carry out everyday tasks. Alzheimer's disease is the most common type of dementia, but there are other types, too.</p>
      <p>If you are concerned about or experiencing memory loss, it's important to talk to your doctor. The following pages can help you start the conversation.</p>
    </div>
    <div class="intro__photo" role="img" aria-label="Photo of an older man playing a ukulele outdoors under palm trees"></div>
    <div class="band band--bottom"><span class="c-brown" style="width:150px"></span><span class="c-teal" style="flex:1"></span></div>
  </div>

  <div class="panel points">
    <div class="points__photo" role="img" aria-label="Photo of a caregiver's hands resting on an older woman's shoulders"></div>
    <div class="points__body">
      <div class="band band--top"><span class="c-teal" style="width:140px"></span><span class="c-rust" style="flex:1"></span></div>
      <h2 class="points__title">Talking Points for Clinic Visits:</h2>
      <ol>
        <li><span class="num">1</span><span>When should I be concerned?</span></li>
        <li><span class="num">2</span><span>What kind of testing can be done for memory loss?</span></li>
        <li><span class="num">3</span><span>What other things could be causing memory loss?
          <ul><li>Anxiety or depression</li><li>Sleep disorders</li><li>Thyroid problems</li><li>Vitamin deficiencies</li><li>Head injuries</li><li>Dehydration</li><li>Infections<br>(Urinary tract, Respiratory, etc.)<br>Medications</li></ul></span></li>
        <li><span class="num">4</span><span>What happens after diagnosis?
          <ul><li>Are there lifestyle changes that could help?</li><li>What safety measures should be taken?</li><li>What are the signs of certain activities becoming unsafe?</li><li>What community resources are available?</li><li>How can we prepare for progression?</li></ul></span></li>
      </ol>
      <div class="band band--bottom"><span class="c-brown" style="width:60px"></span><span class="c-teal" style="flex:1"></span></div>
    </div>
  </div>

  <div class="panel asks">
    <div class="band band--top"><span class="c-dark" style="width:170px"></span><span class="c-rust" style="flex:1"></span></div>
    <div class="asks__text">
      <h2 class="asks__title">Questions Your Doctor<br>May Ask You:</h2>
      <p class="asks__by">Suggested by Dr. Halvorsen</p>
      <ul>
        <li>When did your symptoms of forgetfulness begin?</li>
        <li>What tasks do you find difficult?</li>
        <li>What specific behaviors related to memory loss are concerning you?</li>
        <li>Have you recently been sick?</li>
        <li>Have you recently been in an accident?</li>
        <li>Have you recently fallen or hit your head?</li>
        <li>Have you recently had a loss of someone who is close to you?</li>
        <li>Have there been any recent major changes in your life?</li>
        <li>Have you been dealing with a stressful event in your life?</li>
      </ul>
    </div>
    <div class="asks__photo" role="img" aria-label="Photo of a patient and a doctor talking across a desk in a clinic"></div>
  </div>
</section>

</body>
</html>
```